Dieser Designer hat seinen Job wirklich makellos erledigt. Er war auch bei der Menge an Anforderungen, die ich an ihn hatte, sehr geduldig und wurde allen Anforderungen mehr als gerecht. Ich wäre sehr erfreut, wenn ich in der Zukunft wieder mit ihm arbeiten kann. Ich sehe eine helle Zukunft für diesen Designer und kann ihn nur jedem weiterempfehlen, der Wert auf sein Produkt legt.
Zielgruppe
Genre: Ratgeber
Autorenname: Kilian Sturmfeld
Titel: Staatswesen klar gemacht
Untertitel: Wie Sie endlich mitreden, Ihr Wissen über die deutsche Politik auffrischen und das Land mitgestalten können - Das Politik Buch für Einsteiger
Zielgruppe:
- Personen die Schwierigkeiten haben nachzuvollziehen, was in der Politik geschieht
- Personen die keine Zeit haben, sich durch Nachschlagewerke und co. zu wälzen
- Personen, denen die Wahlentscheidung aufgrund, deren mangelnden Wissens schwer fällt
- Personen, denen das fehlende Wissen über die Politik im Alltag langsam peinlich sind
- Personen, die ihre Meinung in politischen Diskussionen nicht zum Ausdrück bringen können
- Personen, die sich als einzelne machtlos fühlen
- Personen, die mit der politischen Lage unzufrieden sind, jedoch nicht wissen, was wie sein soll
- Personen, die dachten, Politik ist zu langweilig und trocken um sich damit auseinander zu setzen
- Männlich und Weiblich ausgeglichene Zielgruppe
- U.a. junge Leser
Aufgabenstellung
Das ist das Besondere an meinem Buch:
- Die Leser dieses Buches werden in der schnellstmöglichen Zeit ihre politische Unwissenheit besiegen, ohne dass ihnen langweilig wird.
Das sollte meine Leser beim Cover fühlen:
- Sie sollen beim ansehen des Covers das Verlangen verspüren, die Details des Covers erkunden zu wollen.
- Sie sollen sofort erkennen, worum es in dem Buch geht
Das möchte ich besonders hervorheben:
- Ich möchte hervorheben, dass dieses Buch das hochwertigste Buch dieser Thematik ist.
Ich bevorzuge folgende Farben: Helle Farben
Verlagsname und Autorenname dort einfügen wo es am besten passt.
Fonts: Frei Wählbar
Format: Geplant sind 13,34 x 20,32 cm.
Weitere Vorgaben:
- Keine Bilder von echten Personen verwenden
- Seit Kreativ und gestaltet ein ins Auge springendes Cover

```html
<!DOCTYPE html>
<html lang="de">
<head>
<meta charset="utf-8">
<title>Staatswesen klar gemacht – Buchumschlag</title>
<link rel="stylesheet" href="https://fonts.googleapis.com/css2?family=Poppins:wght@500;600;700;800&family=Baloo+2:wght@800&family=Fjalla+One&display=swap">
<style>
  :root {
    --paper: #f5ebdc;
    --page-bg: #f4f4f3;
    --ink: #262626;
    --pink: #f6b9bf;
    --pink-deep: #f2a7ad;
    --peach: #f2d3ae;
    --taupe: #bcb5ac;
    --orange: #ee6236;
    --yellow: #f7c93a;
    --grey: #6c7071;
    --white: #ffffff;
  }
  * { margin: 0; padding: 0; box-sizing: border-box; }
  html, body { width: 1200px; height: 881px; overflow: hidden; background: var(--page-bg); }
  .canvas { position: relative; width: 1200px; height: 881px; }

  .cover {
    position: absolute; top: 70px; width: 480px; height: 740px;
    background: var(--paper); overflow: hidden;
    box-shadow: 0 10px 30px rgba(0,0,0,.15);
  }
  .cover--front { left: 105px; }
  .cover--back { left: 615px; }

  .brush-bands { position: absolute; left: 0; top: 0; width: 480px; height: 240px; }

  .author {
    position: absolute; top: 36px; width: 100%; text-align: center;
    font: 700 20px/1 "Poppins", sans-serif; letter-spacing: .22em; color: var(--ink);
  }
  .title {
    position: absolute; top: 80px; width: 100%; text-align: center;
    font: 800 44px/1.25 "Poppins", sans-serif; color: var(--ink); letter-spacing: .02em;
    text-transform: uppercase;
  }
  .subtitle {
    position: absolute; top: 250px; left: 30px; right: 30px; text-align: center;
    font: 600 12.5px/1.55 "Poppins", sans-serif; letter-spacing: .14em; color: #3a3a3a;
    text-transform: uppercase;
  }
  .badge {
    position: absolute; left: 282px; top: 318px; width: 160px; height: 150px;
    border-radius: 52% 48% 50% 50% / 55% 50% 50% 45%;
    background: var(--orange); color: var(--white);
    display: flex; align-items: center; justify-content: center; text-align: center;
    font: 800 21px/1.2 "Baloo 2", sans-serif; text-transform: uppercase; z-index: 2;
  }
  .illustration {
    position: absolute; left: 0; bottom: 0; width: 100%; height: 330px;
    background: linear-gradient(180deg, var(--paper) 0%, #f0b78f 30%, var(--orange) 55%, var(--yellow) 78%, var(--grey) 100%);
  }
  .front-footer {
    position: absolute; bottom: 24px; left: 42px; right: 24px;
    display: flex; justify-content: space-between; align-items: flex-end;
    font: 700 20px/1 "Poppins", sans-serif; letter-spacing: .2em; color: var(--white);
  }

  .back-illustration {
    position: absolute; left: 0; bottom: 0; width: 100%; height: 420px;
    background: linear-gradient(180deg, rgba(245,235,220,0) 0%, #efcdb5 35%, #f3d9a0 65%, #c9beb3 100%);
    opacity: .85;
  }
  .back-title {
    position: absolute; top: 50px; width: 100%; text-align: center;
    font: 700 33px/1.25 "Poppins", sans-serif; color: var(--orange); text-transform: uppercase;
  }
  .back-content { position: absolute; top: 150px; left: 34px; right: 34px; color: var(--ink); }
  .tagline { font: 600 13px/1.4 "Poppins", sans-serif; margin-bottom: 22px; }
  .benefits { list-style: none; }
  .benefits li {
    font: 500 12.5px/1.5 "Poppins", sans-serif; text-align: justify; margin-bottom: 18px;
  }
  .benefits li::before { content: "· "; }
  .call-to-action {
    position: absolute; top: 560px; left: 30px; right: 30px; text-align: center;
    font: 400 27px/1.3 "Fjalla One", sans-serif; color: #111;
  }
</style>
</head>
<body>
<main class="canvas">

  <section class="cover cover--front" aria-label="Vorderseite">
    <svg class="brush-bands" viewBox="0 0 480 240" aria-hidden="true">
      <path d="M60 2 L470 8 L468 22 L70 20 Z" fill="var(--taupe)"/>
      <path d="M30 18 L470 24 L476 84 L20 90 L40 60 Z" fill="var(--pink-deep)"/>
      <path d="M10 70 L478 76 L472 140 L14 146 L30 110 Z" fill="var(--pink)"/>
      <path d="M0 140 L470 136 L476 150 L8 156 Z" fill="var(--white)"/>
      <path d="M0 150 L466 152 L460 222 L20 226 L0 200 Z" fill="var(--peach)"/>
    </svg>
    <p class="author">KILIAN STURMFELD</p>
    <h1 class="title">Staatswesen<br>klar gemacht</h1>
    <p class="subtitle">Wie Sie endlich mitreden, Ihr Wissen über die deutsche Politik auffrischen und das Land mitgestalten können</p>
    <div class="badge">Das Politik<br>Buch für<br>Einsteiger</div>
    <div class="illustration" role="img" aria-label="Illustration: Silhouetten von Menschen in Orange, Gelb und Grau vor Deutschlandfahnen"></div>
    <div class="front-footer">
      <span class="publisher">VELTRANO</span>
      <span class="genre">RATGEBER</span>
    </div>
  </section>

  <section class="cover cover--back" aria-label="Rückseite">
    <svg class="brush-bands" viewBox="0 0 480 240" aria-hidden="true">
      <path d="M0 0 L480 0 L480 100 L40 112 L0 100 Z" fill="var(--peach)"/>
      <path d="M20 110 L470 96 L476 120 L30 128 Z" fill="#f7e2c8"/>
    </svg>
    <div class="back-illustration" role="img" aria-label="Verblasste Illustration: Silhouetten von Menschen vor Deutschlandfahnen"></div>
    <h2 class="back-title">Staatswesen<br>klar gemacht</h2>
    <div class="back-content">
      <p class="tagline">Souverän und sicher durch jedes Politikgespräch</p>
      <ul class="benefits">
        <li>Dank „Staatswesen klar gemacht“ werden Sie beim Lesen von Nachrichten nicht mehr von Überlegungen abgelenkt, was diese oder jene Begriffe zu bedeuten haben.</li>
        <li>Sie bilden außerdem faktenbasiert eine eigene, gut begründete Meinung und können politische Diskussionen auf Augenhöhe verfolgen und sogar souverän führen.</li>
        <li>Sie erkennen die Probleme der aktuellen Politik und können somit frühzeitig erkennen was für berufliche wie private Folgen auf Ihr Leben haben könnte.</li>
        <li>Mit Ihrem Wissen können Sie andere Menschen aufklären und für die Zusammenhänge der aktuellen Lage begeistern.</li>
      </ul>
    </div>
    <p class="call-to-action">Worauf warten Sie noch? Gestalten<br>Sie jetzt unsere Zukunft mit!</p>
  </section>

</main>
</body>
</html>
```